Attractive Flyer for Moving Company

Our Company is called "Harborline Haulers".
We provide moving service for home and businesses
We need a flyer for a moving company, located in South Florida USA
Flyer size will be 7 x 5 inches, double sided.

Flyer needs to be very attractive and catchy for eye. I want people to keep it even if they don't need our service. I attached a lot of text in separate word file.
Logo, brief and additional pictures are attached.

```html
<!DOCTYPE html>
<html lang="en">
<head>
<meta charset="utf-8">
<title>Harborline Haulers – Your Special Deal</title>
<link rel="stylesheet" href="https://fonts.googleapis.com/css2?family=Montserrat:ital,wght@1,900&family=Open+Sans:ital,wght@0,400;0,600;0,700;1,400&family=Catamaran:wght@800&display=swap">
<style>
  :root {
    --red: #ec1c24;
    --yellow: #fff200;
    --grey: #c2c1bf;
    --ink: #111111;
    --white: #ffffff;
  }
  * { margin: 0; padding: 0; box-sizing: border-box; }
  html, body { width: 1200px; height: 857px; overflow: hidden; background: var(--white); }
  .flyer {
    position: relative;
    width: 1200px;
    height: 857px;
    overflow: hidden;
    background: var(--white);
    font-family: "Open Sans", Arial, sans-serif;
    color: var(--ink);
  }
  .backdrop { position: absolute; inset: 0; }
  .flyer p, .flyer h1, .flyer h2, .flyer ul { position: absolute; white-space: nowrap; }

  .deal-title {
    left: 64px; top: 82px;
    font-family: "Montserrat", Arial, sans-serif;
    font-style: italic; font-weight: 900;
    font-size: 45px; letter-spacing: -2px;
    color: var(--red);
  }
  .deal-note {
    left: 0; width: 640px; top: 130px; text-align: center;
    font-style: italic; font-size: 16px;
  }
  .savings {
    left: 0; width: 640px; top: 164px; text-align: center;
    font-family: "Catamaran", Arial, sans-serif; font-weight: 800;
    font-size: 52px; line-height: 1;
  }
  .savings-sub {
    left: 0; width: 640px; top: 202px; text-align: center;
    font-size: 38px; line-height: 1.2;
  }
  .price {
    font-family: "Open Sans", Arial, sans-serif; font-weight: 700;
    font-size: 32px; color: var(--red); line-height: 1;
  }
  .price--two { left: 112px; top: 265px; }
  .price--three { left: 107px; top: 329px; }
  .service { font-size: 22px; line-height: 28px; }
  .service--two { left: 224px; top: 263px; }
  .service--three { left: 210px; top: 327px; }
  .supplies { left: 110px; top: 396px; font-size: 22px; font-weight: 600; }
  .included-title {
    left: 74px; top: 451px; font-size: 22px; font-weight: 700; color: var(--red);
  }
  .included-list {
    left: 74px; top: 488px; list-style: none; font-size: 22.5px; line-height: 29px;
  }
  .included-list li { position: relative; padding-left: 31px; margin-bottom: 4px; }
  .included-list li::before { content: "•"; position: absolute; left: 0; }
  .rule {
    position: absolute; left: 74px; top: 658px; width: 488px; height: 2px; background: var(--ink);
  }
  .validity {
    left: 74px; top: 667px; font-size: 22px; font-weight: 700; line-height: 29px; color: var(--red);
  }
</style>
</head>
<body>
<main class="flyer">
  <svg class="backdrop" width="1200" height="857" viewBox="0 0 1500 1071" aria-hidden="true">
    <rect class="top-band" x="0" y="0" width="700" height="82" fill="var(--grey)"/>
    <polygon class="price-bar" points="112,323 840,323 845,400 88,400" fill="var(--grey)"/>
    <polygon class="price-bar" points="85,407 845,407 848,485 55,485" fill="var(--grey)"/>
    <polygon class="price-tag" points="112,323 268,323 255,400 88,400" fill="var(--yellow)"/>
    <polygon class="price-tag" points="85,407 250,407 235,485 55,485" fill="var(--yellow)"/>
    <path class="ring" fill="var(--red)" fill-rule="evenodd"
      d="M310,470 m-600,0 a600,600 0 1,0 1200,0 a600,600 0 1,0 -1200,0 Z
         M330,440 m-530,0 a530,530 0 1,0 1060,0 a530,530 0 1,0 -1060,0 Z"/>
    <path class="swoosh" fill="var(--ink)"
      d="M868,845 Q800,990 600,1071 L640,1071 Q820,975 868,845 Z"/>
  </svg>

  <h1 class="deal-title">YOUR SPECIAL DEAL</h1>
  <p class="deal-note">(Cannot be used with any other promotions or coupons)</p>
  <h2 class="savings">SAVE 15% -25%</h2>
  <p class="savings-sub">on your move</p>

  <p class="price price--two">$275</p>
  <p class="service service--two">3 hours of Moving Service<br>with 2 PRO MOVERS</p>
  <p class="price price--three">$325</p>
  <p class="service service--three">3 hours of Moving Service<br>with 3 PRO MOVERS</p>

  <p class="supplies">+ 20% OFF boxes and packing supplies.</p>

  <p class="included-title">INCLUDED IN PRICE</p>
  <ul class="included-list">
    <li>Protection of your furniture with specialized<br>blankets and plastic wrap.</li>
    <li>Disassembly and reassembly of your furniture.</li>
    <li>Wardrobe boxes for the duration of moving<br>process.</li>
  </ul>

  <div class="rule"></div>
  <p class="validity">Keep this voucher, it is valid until<br>January 1st, 2020</p>
</main>
</body>
</html>
```